New Menu Design for edgy barbershop (with bar)

We have a basic graphic for a brand new membership menu. The menu will be located on the wall in our lobby area -- we are planning on making this a very large graphic, but I don't have exact dimensions.

We are a barbershop with a bar & the hottest lady barbers around. We strive to keep a western / saloon feel throughout the barbershop. We cater to mostly a male clientele, so want to have a masculine feel to any creative additions.

I have attached the graphic we started with -- we want to keep the general set up and flow, but are open to your creative brilliance! Our logo is also attached & you can get a good feel for our style on our website: www.ridgelinetrim.example or on our Facebook page: www.facebook.com/ridgelinetrim.

Let me know if you have any questions, or if you need more detail on any of these elements!

A few key details:
- All designs should be horizontal
- The main focus is on the memberships. We want these to pop, and wow customers -- attention should focus on memberships in the graphic, draw the eye in and look glorious.
- We won't look at designs that are too busy or cluttered. Needs to be easy to read & not overwhelming (even with all the information)
- Not too keen on background imagery or color splashes as these make it too complicated. The visual interest should be in how awesome the memberships are!
- Needs to have a clean, masculine feel. Less is more with the background graphics & focus is on getting the info out and drawing people into the awesome memberships we sell.

Target Market(s)

Men 21-65

Font styles to use
Sans Serif

Requirements
Must have
• Masculine feel, western / Saloon theme. Must have all the info included in the graphic slide.
• - Must be Horizontal
• - Must focus on the memberships (need to make the "wow" and drive people to buy them.
Nice to have
• Additional creative elements that really showcase the memberships as awesome!
Should not have
• - No vertical layouts
• - Overly added graphics or background imagery

```html
<!DOCTYPE html>
<html lang="en">
<head>
<meta charset="utf-8">
<title>Ridgeline Trim – Membership Menu</title>
<link rel="stylesheet" href="https://fonts.googleapis.com/css2?family=Rye&family=Oswald:wght@400&family=Quicksand:wght@400;500&family=Mulish:ital,wght@1,300;1,400&display=swap">
<style>
  :root {
    --orange: #e8772e;
    --red: #e4173b;
    --ink: #2a2a2a;
    --paper: #ffffff;
    --backdrop: #d9d9d9;
    --perk-ink: #555555;
  }
  * { margin: 0; padding: 0; box-sizing: border-box; }
  html, body { width: 1200px; height: 848px; overflow: hidden; background: var(--backdrop); }
  .menu {
    position: relative; width: 1200px; height: 848px; background: var(--backdrop);
    font-family: "Quicksand", sans-serif; color: var(--ink);
  }
  .sheet { position: absolute; left: 36px; top: 40px; width: 1124px; height: 772px; background: var(--paper); }

  .brand {
    position: absolute; left: 212px; top: 118px; width: 320px; text-align: center; white-space: nowrap;
    font-family: "Rye", serif; font-size: 34px; color: var(--orange); line-height: 1;
  }
  .brand-dot { display: inline-block; width: 10px; height: 10px; background: var(--orange); border-radius: 50%; vertical-align: middle; margin-right: 10px; }

  .section-title {
    position: absolute; left: 72px; top: 203px; text-transform: uppercase;
    font-family: "Rye", serif; font-size: 19px; font-weight: 400; color: var(--orange); white-space: nowrap;
  }

  .service { position: absolute; white-space: nowrap; }
  .service-head { font-size: 11px; line-height: 14px; margin-bottom: 2px; }
  .service-head .star { color: var(--red); font-size: 11px; margin-right: 4px; }
  .service-name { font-family: "Oswald", sans-serif; text-transform: uppercase; color: var(--red); font-size: 10.5px; letter-spacing: 0.2px; }
  .service-price { color: var(--red); font-size: 12px; margin-left: 8px; font-weight: 500; }
  .service-desc { padding-left: 14px; font-size: 12.5px; line-height: 17px; letter-spacing: 0.2px; }
  .col-right .service-desc { padding-left: 12px; }

  .membership {
    position: absolute; left: 651px; top: 38px; width: 473px; height: 508px;
    background: var(--orange); border-radius: 0 0 14px 14px;
  }
  .membership-title {
    position: absolute; left: 26px; top: 180px; text-transform: uppercase; white-space: nowrap;
    font-family: "Rye", serif; font-size: 22px; font-weight: 400; color: var(--paper);
  }
  .step { position: absolute; left: 28px; font-size: 19px; font-weight: 500; color: var(--ink); white-space: nowrap; }
  .option {
    position: absolute; background: var(--paper); color: var(--orange);
    font-size: 16px; padding: 3px 6px; line-height: 22px; white-space: nowrap;
  }
  .option-num { width: 34px; height: 36px; font-size: 24px; text-align: center; line-height: 30px; padding: 3px 0; }

  .perks-title { position: absolute; left: 654px; top: 561px; font-size: 24px; font-weight: 500; color: var(--orange); white-space: nowrap; }
  .perks-title em { font-style: italic; font-family: "Mulish", sans-serif; font-weight: 400; }
  .perks { position: absolute; left: 654px; top: 594px; width: 460px; list-style: none; }
  .perks li {
    position: relative; padding-left: 50px; font-family: "Mulish", sans-serif; font-style: italic; font-weight: 300;
    font-size: 20px; line-height: 23px; color: var(--perk-ink); margin-bottom: 1px;
  }
  .perks li::before { content: "•"; position: absolute; left: 0; font-style: normal; }
</style>
</head>
<body>
<div class="menu">
  <div class="sheet"></div>

  <div class="brand"><span class="brand-dot"></span>Ridgeline Trim</div>

  <h2 class="section-title">Haircut Services</h2>

  <div class="col-left">
    <div class="service" style="left:72px;top:234px;">
      <div class="service-head"><span class="star">★</span><span class="service-name">The Cowboy Cut</span><span class="service-price">$25</span></div>
      <p class="service-desc">Our full service cut. Hair Cut,<br>Hot Towel, Double Trough Wash,<br>and Straight Razor Neck Shave.</p>
    </div>
    <div class="service" style="left:72px;top:311px;">
      <div class="service-head"><span class="star">★</span><span class="service-name">The Cowgirl Cut</span><span class="service-price">$25</span></div>
      <p class="service-desc">Our Ladies Cut. Hair Cut, Trough<br>Wash.</p>
    </div>
    <div class="service" style="left:72px;top:372px;">
      <div class="service-head"><span class="star">★</span><span class="service-name">The Dusty</span><span class="service-price">$17</span></div>
      <p class="service-desc" style="margin-top:8px">Haircut, Double Trough Wash, Hot<br>Towel, and Straight Razor Neck<br>Shave. This is for cowboys that<br>haven't been blessed with a full head<br>of hair. We know it's not fair, that's<br>why your price is!</p>
    </div>
    <div class="service" style="left:72px;top:517px;">
      <div class="service-head"><span class="star">★</span><span class="service-name">Buzzed Cowboy</span><span class="service-price">$22</span></div>
      <p class="service-desc">Buzz Cut &amp; two beers, for the<br>straightforward cowboy. Must be 21+<br>for this bad boy.</p>
    </div>
    <div class="service" style="left:72px;top:607px;">
      <div class="service-head"><span class="star">★</span><span class="service-name">The Little Cowboy and Cowgirl</span><span class="service-price">$22</span></div>
      <p class="service-desc">Kids Cuts 14 and under Hair Cut,<br>Trough Wash, and Neck Trim.</p>
    </div>
    <div class="service" style="left:72px;top:671px;">
      <div class="service-head"><span class="star">★</span><span class="service-name">The Cowboy Package</span><span class="service-price">$35</span></div>
      <p class="service-desc">Cowboy and Little Cowboy Hair Cut.</p>
    </div>
    <div class="service" style="left:72px;top:725px;">
      <div class="service-head"><span class="star">★</span><span class="service-name">Cowboy Razor Fade</span><span class="service-price">$30</span></div>
      <p class="service-desc">Razor Fade, Hot Towel, Double<br>Wash.</p>
    </div>
  </div>

  <div class="col-right">
    <div class="service" style="left:366px;top:245px;">
      <div class="service-head"><span class="star">★</span><span class="service-name">The Double Scrape</span><span class="service-price">$30</span></div>
      <p class="service-desc">We will take a not so rusty straight<br>razor and get rid of your winter<br>scruff. A face shave with and<br>against the grain.</p>
    </div>
    <div class="service" style="left:366px;top:354px;">
      <div class="service-head"><span class="star">★</span><span class="service-name">The Scalp Scrape</span><span class="service-price">$30</span></div>
      <p class="service-desc">We will take a not so rusty straight<br>razor and get rid of your carrot<br>top.</p>
    </div>
    <div class="service" style="left:366px;top:436px;">
      <div class="service-head"><span class="star">★</span><span class="service-name">The Colorado</span><span class="service-price" style="margin-left:24px">$10</span></div>
      <p class="service-desc">Electric trim your man bush(beard)<br>just how you like it!</p>
    </div>
    <div class="service" style="left:366px;top:494px;">
      <div class="service-head"><span class="star">★</span><span class="service-name">Rough Rider</span><span class="service-price">$10</span></div>
      <p class="service-desc">Straight razor back of the neck<br>shave &amp; two beers to keep your trail<br>rides smooth.</p>
    </div>
    <div class="service" style="left:366px;top:570px;">
      <div class="service-head"><span class="star">★</span><span class="service-name">Eyebrow Wax</span><span class="service-price">$10</span></div>
      <p class="service-desc" style="margin-top:4px">We can wax them both off, one off,<br>or just touch them up. Add on to any<br>cut.</p>
    </div>
  </div>

  <section class="membership">
    <h2 class="membership-title">Choose Your Own Membership</h2>

    <p class="step" style="top:222px;">Step One - Choose Your Service</p>
    <span class="option" style="left:27px;top:250px;">Cowboy</span>
    <span class="option" style="left:152px;top:250px;">Little Cowboy</span>
    <span class="option" style="left:363px;top:250px;">Shave</span>

    <p class="step" style="top:299px;">Step Two - Choose Your Visits(in weeks):</p>
    <span class="option option-num" style="left:29px;top:325px;">1</span>
    <span class="option option-num" style="left:112px;top:325px;">2</span>
    <span class="option option-num" style="left:196px;top:325px;">3</span>
    <span class="option option-num" style="left:284px;top:325px;">4</span>
    <span class="option option-num" style="left:372px;top:325px;">5</span>

    <p class="step" style="top:383px;">Step Three - Choose Your Extras:</p>
    <span class="option" style="left:27px;top:413px;width:99px;">Free beer</span>
    <span class="option" style="left:211px;top:413px;width:127px;">Eyebrow Wax</span>
    <span class="option" style="left:31px;top:452px;width:94px;">Colorado</span>
    <span class="option" style="left:211px;top:452px;">Unlimited. Neck Shaves</span>
  </section>

  <h3 class="perks-title">The Perks <em>(included with all memberships)</em></h3>
  <ul class="perks">
    <li>Discounts on additional services, products &amp;drinks!</li>
    <li>Reduced rate for private parties &amp; after-hoursevents!</li>
    <li>Deals for friends &amp; referral bonuses for you!</li>
    <li>Additional specials, invitations &amp; access throughout the year!</li>
  </ul>
</div>
</body>
</html>
```